Brightway Haul & Repair Services, are a company that offers a 'one stop shop' pre-move clean up a

I have already selected a logo which I would like on the front of the business cards along with phone numbers, web address and email which are:
0419574302
www.brightwayhaul.com.au
brightwayhaulrepair@mailbox.example

On the back of the card I would like to list some of the types of service we offer (clean - move - repairs/maintenance) which are:
CLEAN - windows, gutters, solar panels, driveways/paths, carpets.
MOVE - Small/medium size house/office moves, large item pick-up & delivery, yard clean-up and removal.
General maintenance and repairs.

I would like the blue logo on a gray background.

Thanks

```html
<!DOCTYPE html>
<html lang="en">
<head>
<meta charset="utf-8">
<title>Brightway Haul &amp; Repair Services – Business Cards</title>
<link rel="stylesheet" href="https://fonts.googleapis.com/css2?family=Open+Sans:wght@400;600;700&display=swap">
<style>
  :root {
    --backdrop: #d9dadc;
    --card: #ffffff;
    --blue-deep: #1f6bb5;
    --blue-light: #7dbbe8;
    --ink: #1d1d1f;
    --white: #ffffff;
  }
  * { margin: 0; padding: 0; box-sizing: border-box; }
  html, body { width: 1200px; height: 1004px; overflow: hidden; }
  body {
    background: var(--backdrop);
    font-family: "Open Sans", Arial, sans-serif;
    position: relative;
  }
  .card {
    position: absolute;
    width: 790px;
    height: 451px;
    background: var(--card);
    overflow: hidden;
    box-shadow: 0 2px 6px rgba(0,0,0,0.25);
  }
  .card--front { left: 55px; top: 30px; }
  .card--back  { left: 365px; top: 525px; }

  .card__band {
    position: absolute;
    left: 0; right: 0; bottom: 0;
    height: 160px;
    background: linear-gradient(180deg, var(--blue-light) 0%, var(--blue-deep) 45%, var(--blue-deep) 100%);
  }

  .brand-name {
    color: var(--blue-deep);
    font-weight: 700;
    line-height: 1;
    text-transform: uppercase;
  }
  .brand-name__main { display: block; font-size: 64px; letter-spacing: -1px; }
  .brand-name__sub  { display: block; font-size: 26px; margin-top: 10px; letter-spacing: 0.5px; }

  .card--front .brand-name { position: absolute; left: 38px; top: 110px; }

  .contact {
    position: absolute;
    right: 26px;
    top: 322px;
    list-style: none;
    text-align: right;
    color: var(--white);
    font-size: 20px;
    line-height: 34px;
  }
  .contact__item { display: flex; justify-content: flex-end; align-items: center; gap: 8px; }
  .contact__icon { width: 15px; height: 15px; flex: none; }

  .card--back .brand-name {
    position: absolute;
    left: 0; right: 0;
    top: 90px;
    text-align: center;
  }
  .services__title {
    position: absolute;
    left: 0; right: 0;
    top: 230px;
    text-align: center;
    color: var(--blue-deep);
    font-size: 30px;
    font-weight: 600;
    letter-spacing: 3px;
  }
  .services__row {
    position: absolute;
    display: flex;
    align-items: baseline;
    gap: 10px;
    font-size: 21px;
    color: var(--ink);
    line-height: 30px;
    white-space: nowrap;
  }
  .services__label { color: var(--blue-deep); font-weight: 600; font-size: 23px; }
  .services__row--clean { left: 50px; top: 288px; }
  .services__row--move  { left: 46px; top: 330px; }
  .services__row--move .services__text { text-align: center; }
  .services__extra {
    position: absolute;
    left: 0; right: 0;
    top: 402px;
    text-align: center;
    color: var(--blue-deep);
    font-size: 24px;
    font-weight: 600;
    letter-spacing: 2px;
  }
</style>
</head>
<body>

  <section class="card card--front" aria-label="Business card front">
    <div class="card__band" role="img" aria-label="Decorative blue band"></div>

    <h1 class="brand-name">
      <span class="brand-name__main">Brightway Haul</span>
      <span class="brand-name__sub">&amp; Repair Services</span>
    </h1>

    <ul class="contact">
      <li class="contact__item">
        <svg class="contact__icon" viewBox="0 0 16 16" aria-hidden="true"><path fill="none" stroke="var(--white)" stroke-width="1.6" d="M4,2 L6,5 L5,7 C6,9 7,10 9,11 L11,10 L14,12 L12,14 C7,14 2,9 2,4 Z"/></svg>
        <span>0419574302</span>
      </li>
      <li class="contact__item">
        <svg class="contact__icon" viewBox="0 0 16 16" aria-hidden="true"><g fill="none" stroke="var(--white)" stroke-width="1.3"><circle cx="8" cy="8" r="6.5"/><ellipse cx="8" cy="8" rx="3" ry="6.5"/><path d="M1.5,8 H14.5 M3,4.5 H13 M3,11.5 H13"/></g></svg>
        <span>www.brightwayhaul.com.au</span>
      </li>
      <li class="contact__item">
        <svg class="contact__icon" viewBox="0 0 16 16" aria-hidden="true"><path fill="var(--white)" d="M1,6 L8,2 L15,6 L15,14 L1,14 Z"/><path fill="none" stroke="var(--blue-deep)" stroke-width="1.2" d="M1,6 L8,10 L15,6"/></svg>
        <span>brightwayhaulrepair@mailbox.example</span>
      </li>
    </ul>
  </section>

  <section class="card card--back" aria-label="Business card back">
    <p class="brand-name">
      <span class="brand-name__main">Brightway Haul</span>
      <span class="brand-name__sub">&amp; Repair Services</span>
    </p>

    <h2 class="services__title">Services we offer</h2>

    <div class="services__row services__row--clean">
      <span class="services__label">CLEAN:</span>
      <span class="services__text">Windows, Gutters, Solar Panels, Driveways/paths, Carpets.</span>
    </div>

    <div class="services__row services__row--move">
      <span class="services__label">MOVE:</span>
      <span class="services__text">Small/medium Size House/office Moves, Large Item Pick-up<br>&amp; Delivery, Yard Clean-up And Removal.</span>
    </div>

    <p class="services__extra">General maintenance and repairs.</p>
  </section>

</body>
</html>
```